Aussie Electrician needs Business Card,

Velkor Electrical Services requires a,business card design.. Company colours are black, flouo orange and silver. Refer to attached photos of company shirt.. I was thinking of basing the business card around the company shirt as company vehicle will be black with similar graphics. The business card will need to include my mobile phone number which is 0400 518 067, my business address which is P.O. Box 863, Narrabeen, N.S.W., 2101, my email which is greg@velkorelectrical.com.au as well as my contractor licence number which is 5143K

Industry/Entity Type

Business

Contact Information for Business Card

mobile: 0400 518 067, email: greg@velkorelectrical.com.au,address :P.O. Box 863 TALLOWMERE NSW 2196, Contractor Lic No 5143K, Greg Halloway

Requirements
Must have
• Refer to photos of shirt. Gloss black background

```html
<!DOCTYPE html>
<html lang="en">
<head>
<meta charset="utf-8">
<title>Velkor Electrical Services – Business Card</title>
<link rel="stylesheet" href="https://fonts.googleapis.com/css2?family=Noto+Serif:wght@700&family=Roboto+Condensed:wght@400&display=swap">
<style>
  :root {
    --page: #e9e7e3;
    --card-white: #ffffff;
    --card-silver: #e4e4e4;
    --gloss-black: #1c1c1c;
    --gloss-mid: #3a3a3a;
    --fluoro-orange: #f07a2e;
    --ink: #1a1a1a;
    --contact-text: #f2f2f2;
    --shirt-dark: #121212;
    --shirt-mid: #2a2a2a;
  }
  * { margin: 0; padding: 0; box-sizing: border-box; }
  html, body {
    width: 1200px; height: 978px; overflow: hidden;
    background: var(--page);
  }
  .business-card {
    position: absolute;
    left: 100px; top: 203px;
    width: 1000px; height: 572px;
    box-shadow: 0 18px 40px rgba(0,0,0,0.25);
    overflow: hidden;
  }
  .card-art { position: absolute; inset: 0; }
  .company-name {
    position: absolute;
    left: 70px; top: 58px;
    font-family: "Noto Serif", serif;
    font-weight: 700;
    font-size: 58px;
    line-height: 1.2;
    color: var(--ink);
  }
  .contact-list {
    position: absolute;
    left: 530px; top: 222px;
    list-style: none;
    font-family: "Roboto Condensed", sans-serif;
    font-size: 30px;
    color: var(--contact-text);
  }
  .contact-list li {
    display: flex; align-items: center; gap: 14px;
    height: 50px;
    white-space: nowrap;
  }
  .contact-icon { width: 20px; height: 22px; flex: none; }
  .holder {
    position: absolute;
    left: 70px; top: 420px;
    font-family: "Roboto Condensed", sans-serif;
  }
  .holder-name {
    font-size: 36px;
    color: var(--fluoro-orange);
    line-height: 1.2;
  }
  .holder-licence {
    font-size: 30px;
    color: var(--contact-text);
    line-height: 1.3;
  }
</style>
</head>
<body>
  <div class="business-card">
    <svg class="card-art" viewBox="0 0 1000 572" width="1000" height="572">
      <defs>
        <linearGradient id="whitePanel" x1="0" y1="0" x2="0" y2="1">
          <stop offset="0" stop-color="var(--card-white)"/>
          <stop offset="1" stop-color="var(--card-silver)"/>
        </linearGradient>
        <linearGradient id="glossBlack" x1="0" y1="0" x2="1" y2="1">
          <stop offset="0" stop-color="var(--gloss-mid)"/>
          <stop offset="0.45" stop-color="var(--gloss-black)"/>
          <stop offset="1" stop-color="#0e0e0e"/>
        </linearGradient>
        <linearGradient id="shirtTone" x1="0" y1="0" x2="1" y2="1">
          <stop offset="0" stop-color="var(--shirt-mid)"/>
          <stop offset="1" stop-color="var(--shirt-dark)"/>
        </linearGradient>
      </defs>
      <rect class="card-base" width="1000" height="572" fill="url(#glossBlack)"/>
      <polygon class="white-panel" points="0,0 1000,0 1000,120 0,320" fill="url(#whitePanel)"/>
      <polygon class="panel-divider" points="0,326 1000,126 1000,131 0,331" fill="var(--fluoro-orange)"/>
      <rect class="photo-frame" x="822" y="14" width="148" height="104" fill="none" stroke="var(--fluoro-orange)" stroke-width="2"/>
      <rect class="shirt-photo" role="img" aria-label="Photo of the black company work shirt with orange graphics" x="834" y="22" width="124" height="88" fill="url(#shirtTone)"/>
    </svg>

    <div class="company-name">Velkor Electrical<br>Services</div>

    <ul class="contact-list">
      <li>
        <svg class="contact-icon" viewBox="0 0 20 22" aria-hidden="true"><path d="M10 1a7 7 0 0 0-7 7c0 5 7 13 7 13s7-8 7-13a7 7 0 0 0-7-7zm0 10a3 3 0 1 1 0-6 3 3 0 0 1 0 6z" fill="var(--fluoro-orange)"/></svg>
        P.O. Box 863 Tallowmere NSW 2196
      </li>
      <li>
        <svg class="contact-icon" viewBox="0 0 20 22" aria-hidden="true"><path d="M5 2l3 5-2 2c1 3 3 5 6 6l2-2 5 3-2 4C10 20 2 12 2 4z" fill="var(--fluoro-orange)"/></svg>
        0400 518 067
      </li>
      <li>
        <svg class="contact-icon" viewBox="0 0 20 22" aria-hidden="true"><rect x="1" y="5" width="18" height="13" fill="var(--fluoro-orange)"/><path d="M1 5l9 7 9-7" fill="none" stroke="var(--gloss-black)" stroke-width="1.5"/></svg>
        greg@velkorelectrical.com.au
      </li>
    </ul>

    <div class="holder">
      <p class="holder-name">Greg Halloway</p>
      <p class="holder-licence">Contractor Lic No 5143K</p>
    </div>
  </div>
</body>
</html>
```